Moder Business Card Design for Renewables Business

Need a business card design for my business. We collect & repurpose spent coffee ground from cafes. The cards will be made from recycled paper. Needs to fit our corporate colour scheme of white, green & brown (see logo for colour codes). Eco friendly, modern, intresting & eye catching.
This card needs to convey the message of the business and fit into its mantra of eco-friendly, sustainable etc.

Target Market(s)

Cafe Owners, Coffee Drinkers, Recycling Companies, Farmers

Industry/Entity Type

Recycling

Contact Information for Business Card

Name; Peter Dalton
Phone; 0438 216 570
e-mail; info@florivex.com.au
website; www.florivex.com.au

Font styles to use
Sans Serif
Script

Colors

Designer to choose colors to be used in the design.

Requirements
Must have
• FRONT;
• Logo, Name (Peter Dalton), phone number, e-mail address, website
• BACK;
• On the back in cursive text; 'SUSTAINABILITY IN THE DAILY GRIND'
• Small facebook & Instagram logos with text 'Florivex'
Should not have
• messy design

```html
<!DOCTYPE html>
<html lang="en">
<head>
<meta charset="utf-8">
<title>Florivex – Business Card</title>
<link href="https://fonts.googleapis.com/css2?family=Montserrat:wght@400;500;700&display=swap" rel="stylesheet">
<style>
  :root {
    --green: #7aa641;
    --brown: #5e2f13;
    --paper: #ffffff;
    --edge: #cfc7c2;
  }
  * { margin: 0; padding: 0; box-sizing: border-box; }
  html, body {
    width: 687px;
    height: 1200px;
    overflow: hidden;
    background: var(--paper);
  }
  .card {
    position: relative;
    width: 687px;
    height: 1200px;
    background: var(--paper);
    border: 1px solid var(--edge);
    font-family: "Montserrat", sans-serif;
    color: var(--brown);
  }
  .band {
    position: absolute;
    left: 0;
    width: 100%;
    height: 10px;
    background: var(--brown);
  }
  .band--top { top: 2px; }
  .band--bottom { bottom: 2px; }

  .brand {
    position: absolute;
    top: 70px;
    left: 0;
    width: 100%;
    text-align: center;
  }
  .brand__mark {
    display: block;
    margin: 0 auto;
    width: 240px;
    height: 240px;
  }
  .brand__name {
    margin-top: 24px;
    font-size: 41px;
    font-weight: 500;
    letter-spacing: 0.5px;
    color: var(--green);
  }

  .person {
    position: absolute;
    top: 526px;
    width: 100%;
    text-align: center;
    font-size: 50px;
    font-weight: 700;
    letter-spacing: 0.5px;
  }
  .person__first { color: var(--green); }
  .person__last { color: var(--brown); }

  .contacts {
    position: absolute;
    top: 728px;
    width: 100%;
    list-style: none;
    text-align: center;
  }
  .contact {
    height: 135px;
  }
  .contact__icon {
    display: block;
    margin: 0 auto 8px;
    width: 52px;
    height: 52px;
  }
  .contact__text {
    font-size: 34px;
    font-weight: 500;
    letter-spacing: 1px;
    color: var(--brown);
  }
</style>
</head>
<body>
<main class="card">
  <div class="band band--top"></div>

  <header class="brand">
    <svg class="brand__mark" viewBox="0 0 240 240" aria-hidden="true">
      <circle cx="120" cy="120" r="108" fill="none" stroke="var(--green)" stroke-width="8"/>
    </svg>
    <div class="brand__name">FLORIVEX</div>
  </header>

  <h1 class="person">
    <span class="person__first">Peter</span>
    <span class="person__last">Dalton</span>
  </h1>

  <ul class="contacts">
    <li class="contact">
      <svg class="contact__icon" viewBox="0 0 52 52" aria-hidden="true">
        <circle cx="26" cy="26" r="26" fill="var(--green)"/>
        <path d="M19 14c1.5-1 3-.6 3.8.8l2.4 4.2c.7 1.3.3 2.6-.8 3.4l-1.8 1.2c1 2.8 3.2 5.4 5.8 6.8l1.5-1.6c1-1 2.4-1.1 3.5-.2l3.7 3c1.2 1 1.3 2.5.3 3.7l-1.8 2c-1.5 1.6-4 2-6.2 1-7.3-3.4-12.6-9.9-14.2-17.6-.5-2.4.5-4.6 2.4-5.9z" fill="#fff"/>
      </svg>
      <div class="contact__text">0438 216 570</div>
    </li>
    <li class="contact">
      <svg class="contact__icon" viewBox="0 0 52 52" aria-hidden="true">
        <circle cx="26" cy="26" r="26" fill="var(--green)"/>
        <rect x="13" y="17" width="26" height="18" rx="2" fill="#fff"/>
        <path d="M14 18.5l12 9 12-9" fill="none" stroke="var(--green)" stroke-width="2"/>
      </svg>
      <div class="contact__text">info@florivex.com.au</div>
    </li>
    <li class="contact">
      <svg class="contact__icon" viewBox="0 0 52 52" aria-hidden="true">
        <circle cx="26" cy="26" r="26" fill="var(--green)"/>
        <text x="26" y="34" text-anchor="middle" font-family="Montserrat, sans-serif" font-size="24" font-weight="500" fill="#fff">@</text>
      </svg>
      <div class="contact__text">www.florivex.com.au</div>
    </li>
  </ul>

  <div class="band band--bottom"></div>
</main>
</body>
</html>
```